CRM Application Interface Design

We have a wireframe / design draft for a CRM application (similar to Brimvantle, Kefa, etc.). We need this draft to be restyled to create a more finished, polished application user interface. There is a specific branding color scheme that must be adhered to, but you may add secondary and tertiary colors as needed.
At a minimum, these branding colors are required to appear in the design:
#CC0000 : Primary brand color
#AA0000 : Primary shaded (e.g. hover) color
#DBEEF5 / #4A4A4A : Gray
Some other colors you may wish to add:
* "Error/warning" color of your choice
* "Informational / focus" color of your choice
Two screens are provided, both should be re-styled as you see fit in order to finish the design:
1. "Search for customers" screen
2. "View customer details" screen
Requirements:
1. Must have the navigation along the top, cannot switch to a left nav. Must also remain two-level navigation (primary nav at top with sub nav beneath it).
2. The design must use the primary red color in a thoughtful, balanced way, without overdoing it. Please make use of other colors if needed to offset the use of red.
3. Text must be high enough contrast to be readable. The wireframe/draft screens attached show a "washed-out" low-contrast UI with light gray text. That design theme should not be used in the final design.
Aside from the above requirements, please feel free to think creatively and present substantially different ideas. Some of the things we are open to changing include:
* Element style (eg. square vs. rounded corners, flat vs. depth)
* Use of color vs. grayscale
* Menus and navigation
* Light / dark theme
* Any other stylistic elements
* Minor layout changes can be made if needed, but elements should not be moved if that can be avoided.
Goals:
* This is a business application that is used frequently and for long periods, so should not have any unnecessary distracting elements.
* Looking for a design that is clean, professional, readable, usable, and intuitive.

```html
<!DOCTYPE html>
<html lang="en">
<head>
<meta charset="utf-8">
<title>People Search</title>
<link href="https://fonts.googleapis.com/css2?family=Lato:wght@400;700;900&display=swap" rel="stylesheet">
<style>
:root{
  --brand:#CC0000;
  --brand-dark:#AA0000;
  --ink:#4A4A4A;
  --ink-strong:#2b2b2b;
  --muted:#6d6d6d;
  --line:#dfe3e6;
  --bg:#eef1f3;
  --select:#DBEEF5;
  --card:#ffffff;
  --star:#f5a623;
  --head:#7d8d96;
}
*{box-sizing:border-box;margin:0;padding:0}
html,body{width:766px;height:1200px;overflow:hidden}
body{font-family:"Lato",sans-serif;color:var(--ink);background:var(--bg);font-size:11px}
.topbar{height:42px;background:var(--card);display:flex;align-items:center;padding:0 22px;border-bottom:1px solid var(--line)}
.brand{display:flex;align-items:center;width:150px}
.brand-name{font-weight:700;font-size:14px;color:var(--ink-strong);letter-spacing:.5px}
.primary-nav{display:flex;gap:24px;margin-left:70px}
.primary-nav a{font-size:11px;font-weight:700;color:var(--ink);text-decoration:none}
.primary-nav a.active{color:var(--brand)}
.utility{margin-left:auto;display:flex;align-items:center;gap:14px;font-size:10px;font-weight:700}
.avatar{width:22px;height:22px;border-radius:50%;background:#c7cdd1}
.subnav{height:26px;background:var(--card);display:flex;justify-content:center;gap:26px;border-bottom:1px solid var(--line)}
.subnav a{font-size:10px;color:var(--ink);text-decoration:none;line-height:24px;font-weight:700}
.subnav a.active{color:var(--brand);border-bottom:2px solid var(--brand)}
.page{padding:0 38px}
.page-head{display:flex;align-items:center;margin-top:50px}
.page-title{font-size:18px;font-weight:400;color:var(--ink-strong)}
.page-title b{font-weight:700}
.actions{margin-left:auto;display:flex;gap:6px}
.btn{font:700 9px "Lato",sans-serif;padding:7px 12px;border:1px solid #c9cfd3;background:var(--card);color:var(--ink);border-radius:2px;letter-spacing:.3px}
.btn.primary{background:var(--brand);border-color:var(--brand);color:#fff;padding:7px 20px}
.btn.outline{border-color:var(--brand);color:var(--brand)}
.filters{display:flex;flex-wrap:wrap;gap:7px;margin-top:22px;width:540px}
.chip{font-size:8.5px;font-weight:700;background:#d9dee2;color:var(--ink-strong);padding:5px 10px;border-radius:12px}
.chip i{font-style:normal;margin-left:5px;color:var(--muted)}
.card{background:var(--card);margin-top:44px;border-radius:2px;box-shadow:0 1px 3px rgba(0,0,0,.08);padding:18px 0 0}
.card-head{padding:0 14px}
.card-title{font-size:15px;font-weight:700;color:var(--ink-strong)}
.toolbar{display:flex;align-items:center;margin-top:14px;position:relative}
.search{width:160px;height:24px;border:1px solid #c9cfd3;border-radius:2px;display:flex;align-items:center;justify-content:space-between;padding:0 8px;color:var(--muted);font-size:9px}
.tools{margin-left:auto;display:flex;align-items:center;gap:10px;position:relative}
.icon-btn{width:22px;height:22px;border-radius:50%;background:var(--brand);display:flex;align-items:center;justify-content:center}
.tooltip{position:absolute;left:-6px;top:-24px;background:var(--ink-strong);color:#fff;font-size:8px;padding:3px 6px;border-radius:2px}
table{width:100%;border-collapse:collapse;margin-top:12px;table-layout:fixed}
th{background:var(--head);color:#fff;font-size:8px;font-weight:700;text-align:left;height:22px;padding:0 6px;letter-spacing:.3px}
td{height:34px;padding:0 6px;border-bottom:1px solid var(--line);font-size:9px;color:var(--ink);white-space:nowrap;overflow:hidden}
td.name{font-weight:700;color:var(--ink-strong)}
tr.selected td{background:var(--select)}
.box{width:10px;height:10px;border:1px solid #9aa3a8;border-radius:1px;display:block;background:#fff}
.box.on{background:var(--brand);border-color:var(--brand)}
.action{color:var(--brand);font-weight:900;font-size:9px}
.card-foot{display:flex;align-items:center;padding:14px}
.pager{margin-left:auto;display:flex;gap:4px}
.pager span{width:18px;height:18px;border:1px solid #c9cfd3;font-size:9px;display:flex;align-items:center;justify-content:center;border-radius:2px}
.pager span.current{background:var(--brand);border-color:var(--brand);color:#fff}
</style>
</head>
<body>
<header class="topbar">
  <div class="brand"><span class="brand-name">Corvane</span></div>
  <nav class="primary-nav">
    <a href="#">Dashboard</a><a href="#" class="active">Customers</a><a href="#">Admin</a><a href="#">Sales</a><a href="#">Settings</a>
  </nav>
  <div class="utility"><span>● Location ▾</span><span>★ Favorites ▾</span><span class="avatar"></span></div>
</header>
<nav class="subnav"><a href="#" class="active">Search</a><a href="#">Leads</a><a href="#">Projects</a><a href="#">Contacts</a></nav>

<main class="page">
  <div class="page-head">
    <h1 class="page-title"><b>People</b> Search</h1>
    <div class="actions">
      <button class="btn">MODIFY SEARCH</button><button class="btn">SAVE SEARCH</button><button class="btn">NEW CUSTOMER</button><button class="btn primary">SEND EMAIL</button>
    </div>
  </div>
  <div class="filters">
    <span class="chip">JDOE@MAILNEST.COM<i>×</i></span><span class="chip">MAILNEST.COM<i>×</i></span><span class="chip">(555) 010-0199<i>×</i></span><span class="chip">SEATTLE<i>×</i></span><span class="chip">WA<i>×</i></span><span class="chip">98136<i>×</i></span>
    <span class="chip">NO CONNECTION<i>×</i></span><span class="chip">WALLA WALLA<i>×</i></span><span class="chip">HIGH SCHOOL EDUCATION<i>×</i></span><span class="chip">1998-2014<i>×</i></span><span class="chip">05/10/1998<i>×</i></span>
  </div>

  <section class="card">
    <div class="card-head">
      <h2 class="card-title">Search Result</h2>
      <div class="toolbar">
        <div class="search">Search...<svg width="10" height="10" viewBox="0 0 10 10"><circle cx="4" cy="4" r="3" fill="none" stroke="#6d6d6d" stroke-width="1.2"/><line x1="6.3" y1="6.3" x2="9" y2="9" stroke="#6d6d6d" stroke-width="1.2"/></svg></div>
        <div class="tools">
          <span class="tooltip">Delete</span>
          <span class="icon-btn"><svg width="10" height="10" viewBox="0 0 10 10"><rect x="2" y="3" width="6" height="6" fill="#fff"/><rect x="1" y="1.5" width="8" height="1" fill="#fff"/></svg></span>
          <button class="btn outline">EXCEL</button>
        </div>
      </div>
    </div>
    <table>
      <colgroup><col style="width:26px"><col style="width:22px"><col style="width:118px"><col style="width:84px"><col style="width:64px"><col style="width:170px"><col style="width:120px"><col style="width:86px"></colgroup>
      <thead><tr><th><span class="box"></span></th><th></th><th>NAME</th><th>OFFICE</th><th>LOGIN ID</th><th>PRIMARY EMAIL</th><th>PRIMARY PHONE</th><th>MENU</th></tr></thead>
      <tbody>
        <tr class="selected"><td><span class="box on"></span></td><td style="color:var(--star)">★</td><td class="name">Orla Fenwick</td><td>TALVO</td><td></td><td>orla.fenwick@corvane.com</td><td>+1 (555) 010-0101</td><td class="action">ACTION</td></tr>
        <tr class="selected"><td><span class="box on"></span></td><td style="color:var(--star)">★</td><td class="name">Tobias Marlowe</td><td>QUIRBEX</td><td></td><td>tobias.marlowe@corvane.com</td><td>+1 (555) 010-0102</td><td class="action">ACTION</td></tr>
        <tr><td><span class="box"></span></td><td>☆</td><td class="name">Greta Hollis</td><td>NORVIK</td><td>ghollis</td><td>greta.hollis@corvane.com</td><td>+1 (555) 010-0103</td><td class="action">ACTION</td></tr>
        <tr><td><span class="box"></span></td><td>☆</td><td class="name">Nadia Ferrand</td><td>PELLAMO</td><td></td><td>nadia.ferrand@corvane.com</td><td>+1 (555) 010-0104</td><td class="action">ACTION</td></tr>
        <tr><td><span class="box"></span></td><td>☆</td><td class="name">Priya Calder</td><td>VANTORA</td><td></td><td>priya.calder@corvane.com</td><td>+1 (555) 010-0105</td><td class="action">ACTION</td></tr>
        <tr><td><span class="box"></span></td><td>☆</td><td class="name">Ines Whitford</td><td>BRISKEL</td><td></td><td>ines.whitford@corvane.com</td><td>+1 (555) 010-0106</td><td class="action">ACTION</td></tr>
        <tr><td><span class="box"></span></td><td>☆</td><td class="name">Clara Ostrov</td><td>LUMORA</td><td></td><td>clara.ostrov@corvane.com</td><td>+1 (555) 010-0107</td><td class="action">ACTION</td></tr>
        <tr><td><span class="box"></span></td><td>☆</td><td class="name">Malik Dunmore</td><td>HARTVEN</td><td></td><td>malik.dunmore@corvane.com</td><td>+1 (555) 010-0108</td><td class="action">ACTION</td></tr>
        <tr><td><span class="box"></span></td><td>☆</td><td class="name">Leona Pryce</td><td>ORBINEX</td><td></td><td>leona.pryce@corvane.com</td><td>+1 (555) 010-0109</td><td class="action">ACTION</td></tr>
        <tr><td><span class="box"></span></td><td>☆</td><td class="name">Hana Vesely</td><td>SOLVANE</td><td></td><td>hana.vesely@corvane.com</td><td>+1 (555) 010-0110</td><td class="action">ACTION</td></tr>
        <tr class="selected"><td><span class="box on"></span></td><td style="color:var(--star)">★</td><td class="name">Orla Fenwick</td><td>TALVO</td><td></td><td>orla.fenwick@corvane.com</td><td>+1 (555) 010-0101</td><td class="action">ACTION</td></tr>
        <tr class="selected"><td><span class="box on"></span></td><td style="color:var(--star)">★</td><td class="name">Tobias Marlowe</td><td>QUIRBEX</td><td></td><td>tobias.marlowe@corvane.com</td><td>+1 (555) 010-0102</td><td class="action">ACTION</td></tr>
        <tr><td><span class="box"></span></td><td>☆</td><td class="name">Greta Hollis</td><td>NORVIK</td><td>ghollis</td><td>greta.hollis@corvane.com</td><td>+1 (555) 010-0103</td><td class="action">ACTION</td></tr>
        <tr><td><span class="box"></span></td><td>☆</td><td class="name">Nadia Ferrand</td><td>PELLAMO</td><td></td><td>nadia.ferrand@corvane.com</td><td>+1 (555) 010-0104</td><td class="action">ACTION</td></tr>
        <tr><td><span class="box"></span></td><td>☆</td><td class="name">Priya Calder</td><td>VANTORA</td><td></td><td>priya.calder@corvane.com</td><td>+1 (555) 010-0105</td><td class="action">ACTION</td></tr>
        <tr><td><span class="box"></span></td><td>☆</td><td class="name">Ines Whitford</td><td>BRISKEL</td><td></td><td>ines.whitford@corvane.com</td><td>+1 (555) 010-0106</td><td class="action">ACTION</td></tr>
        <tr><td><span class="box"></span></td><td>☆</td><td class="name">Clara Ostrov</td><td>LUMORA</td><td></td><td>clara.ostrov@corvane.com</td><td>+1 (555) 010-0107</td><td class="action">ACTION</td></tr>
        <tr><td><span class="box"></span></td><td>☆</td><td class="name">Malik Dunmore</td><td>HARTVEN</td><td></td><td>malik.dunmore@corvane.com</td><td>+1 (555) 010-0108</td><td class="action">ACTION</td></tr>
        <tr><td><span class="box"></span></td><td>☆</td><td class="name">Leona Pryce</td><td>ORBINEX</td><td></td><td>leona.pryce@corvane.com</td><td>+1 (555) 010-0109</td><td class="action">ACTION</td></tr>
        <tr><td><span class="box"></span></td><td>☆</td><td class="name">Hana Vesely</td><td>SOLVANE</td><td></td><td>hana.vesely@corvane.com</td><td>+1 (555) 010-0110</td><td class="action">ACTION</td></tr>
      </tbody>
    </table>
    <div class="card-foot">
      <span>1–25 of 500 People</span>
      <div class="pager"><span>‹</span><span class="current">1</span><span>2</span><span>3</span><span>4</span><span>›</span></div>
    </div>
  </section>
</main>
</body>
</html>
```